Cleaners Needs Bounce-Back Coupon For Laundry Service

We need a "bounce-back" coupon to attach to peoples dry cleaning orders that offers one free wash-n-fold laundry service. Right now we always attach their receipt to the bag that contains their dry cleaning when we return it. We'd like to also attach a coupon that will entice them to come try our laundry service.

Background on the service: We sort, wash, dry, and fold the laundry for customers and then neatly put it in a nice bag that makes returning very convenient. Their laundry comes out fresh, clean, smelling great, and without the hassle of doing it themselves. We have a great return rate. Most customers that try out the service become long term customers. The goal is to get our dry cleaning customers to come try it out.

Requirements:
* 5" x 8" and one-sided.
* To be printed on a standard color of card stock.
* Must incorporate our logo.
* Needs a place for us to fill in an expiration date. We'll fill in a date about two weeks out from the time they pick up their dry cleaning.
* Limit one coupon per customer.
* Limit 50 pounds of laundry per coupon.

Industry/Entity Type

Dry Cleaning

```html
<!DOCTYPE html>
<html lang="en">
<head>
<meta charset="utf-8">
<title>Bounch Back Coupon – Laundry on Elm</title>
<link rel="stylesheet" href="https://fonts.googleapis.com/css2?family=Archivo+Black&family=Mulish:ital,wght@0,700;0,800;1,800;1,900&display=swap">
<style>
  :root {
    --page: #f1ede4;
    --sky-top: #f4faff;
    --sky-mid: #bfe1f7;
    --sky-low: #4fb0e8;
    --door-dark: #0d4f9c;
    --door-mid: #1f74c9;
    --door-light: #5aa6ea;
    --rim: #8e9aa3;
    --headline: #cde6fb;
    --headline-shadow: #0a2346;
    --coupon-yellow: #ffe51a;
    --ink: #111111;
    --card: #ffffff;
    --brand-blue: #2a5fc0;
  }
  * { margin: 0; padding: 0; box-sizing: border-box; }
  html, body { width: 1200px; height: 988px; overflow: hidden; background: var(--page); }
  .coupon {
    position: absolute; left: 320px; top: 46px; width: 560px; height: 896px; overflow: hidden;
    background:
      linear-gradient(160deg, transparent 38%, rgba(255,255,255,.55) 52%, transparent 66%),
      linear-gradient(180deg, var(--sky-top) 0%, var(--sky-mid) 45%, var(--sky-low) 100%);
    font-family: "Mulish", sans-serif;
    color: var(--ink);
  }
  .washer-art {
    position: absolute; left: 67px; top: 96px; width: 452px; height: 465px;
  }
  .headline {
    position: absolute; left: 96px; top: 165px;
    transform: rotate(-5deg); transform-origin: left top;
    font-family: "Archivo Black", sans-serif; line-height: .92;
  }
  .headline__word {
    display: block; font-size: 90px; color: var(--headline);
    text-shadow: 4px 4px 0 var(--headline-shadow), 6px 6px 0 var(--headline-shadow);
    letter-spacing: -1px;
  }
  .headline__word--indent { margin-left: 12px; }
  .headline__coupon {
    display: block; margin: 8px 0 0 42px; font-size: 58px; color: var(--coupon-yellow);
    text-shadow: 3px 3px 0 var(--ink), 4px 4px 0 var(--ink);
  }
  .ticket {
    position: absolute; left: 58px; top: 520px; width: 298px; height: 146px;
    background: var(--card); border-radius: 14px;
    box-shadow: 3px 4px 8px rgba(0,0,0,.25);
    transform: rotate(-12deg); padding: 14px 18px;
  }
  .ticket__brand { display: flex; align-items: center; gap: 6px; font-size: 14px; font-weight: 800; color: var(--brand-blue); }
  .ticket__mark { width: 14px; height: 14px; background: var(--brand-blue); }
  .ticket__expiry { margin-top: 8px; font-size: 17px; font-weight: 700; padding-bottom: 8px; border-bottom: 1.5px solid #9aa4ad; }
  .ticket__limit { margin-top: 8px; font-size: 14px; font-weight: 900; line-height: 1.15; }
  .ticket__weight { font-size: 12px; font-weight: 700; }
  .brand {
    position: absolute; left: 160px; top: 672px; display: flex; align-items: center; gap: 14px;
  }
  .brand__mark { width: 58px; height: 58px; background: var(--brand-blue); }
  .brand__name { font-size: 44px; font-weight: 800; color: var(--brand-blue); }
  .tagline {
    position: absolute; left: 163px; top: 788px; font-size: 20px; font-weight: 900; font-style: italic; line-height: 1.3;
  }
</style>
</head>
<body>
  <main class="coupon">
    <svg class="washer-art" viewBox="0 0 452 465" role="img" aria-label="Illustration of an open front-loading washer door">
      <defs>
        <radialGradient id="doorTone" cx="45%" cy="40%" r="65%">
          <stop offset="0" stop-color="var(--door-light)"/>
          <stop offset=".6" stop-color="var(--door-mid)"/>
          <stop offset="1" stop-color="var(--door-dark)"/>
        </radialGradient>
      </defs>
      <circle cx="196" cy="240" r="196" fill="url(#doorTone)"/>
    </svg>

    <h1 class="headline">
      <span class="headline__word">Bounch</span>
      <span class="headline__word headline__word--indent">Back</span>
      <span class="headline__coupon">COUPON</span>
    </h1>

    <section class="ticket">
      <div class="ticket__brand"><span class="ticket__mark"></span>Laundry on Elm</div>
      <p class="ticket__expiry">Expiration: 12/ 30 / 14</p>
      <p class="ticket__limit">1 COUPON PER CUSTOMER<br><span class="ticket__weight">50 pounds of laundry per coupon</span></p>
    </section>

    <div class="brand">
      <span class="brand__mark"></span>
      <span class="brand__name">Laundry on Elm</span>
    </div>

    <p class="tagline">With us, your laundry comes out<br>FRESH, CLEAN and SMELLS GREAT</p>
  </main>
</body>
</html>
```